Dorvanski Law Rebrand

I am recreating my law firm website. I got a new logo and would like to recreate the website to match the new logo. the website is dorvanskilaw.com

```html
<!DOCTYPE html>
<html lang="en">
<head>
<meta charset="utf-8">
<title>Dorvanski Law, PLLC</title>
<link href="https://fonts.googleapis.com/css2?family=Montserrat:wght@400;500;600;700;800&display=swap" rel="stylesheet">
<style>
:root{
  --blue:#0a4f8f;
  --blue-dark:#083f73;
  --muted:#8a9bbb;
  --grey-bg:#ececee;
  --text:#333;
  --soft:#666;
  --white:#fff;
}
*{box-sizing:border-box;margin:0;padding:0}
html,body{width:1200px;height:3552px;overflow:hidden}
body{font-family:'Montserrat',sans-serif;color:var(--text);background:var(--white);position:relative}
.abs{position:absolute}
.btn{position:absolute;display:flex;align-items:center;justify-content:center;background:var(--blue);color:var(--white);font-weight:700;font-size:15px;letter-spacing:.3px;text-transform:uppercase;border-radius:2px}
.btn.muted{background:var(--muted)}
.brand{font-weight:600;color:var(--blue);letter-spacing:3px;display:flex;align-items:center;gap:12px}
.brand .dot{width:16px;height:16px;border-radius:50%;background:var(--blue)}
.topbar{left:370px;top:0;width:830px;height:60px;background:var(--blue);clip-path:polygon(0 0,100% 0,100% 100%,45px 100%);display:flex;align-items:center;gap:0;color:var(--white);font-size:13px;font-weight:600}
.topbar .item{position:absolute;display:flex;align-items:center;gap:10px;top:20px}
.nav{top:88px;left:398px;display:flex;gap:28px;font-size:15px;color:#444}
.nav .active{color:var(--blue);font-weight:700;position:relative}
.nav .active::after{content:"";position:absolute;left:0;right:0;bottom:-30px;height:3px;background:var(--blue)}
.hero-photo{left:0;top:132px;width:1200px;height:680px;background:linear-gradient(100deg,#4a3c30 0%,#2a221c 35%,#1e1915 60%,#3a2a1e 100%)}
.hero-title{top:250px;left:0;width:1200px;text-align:center;color:var(--white);font-weight:800;font-size:51px;line-height:66px;letter-spacing:.5px}
.hero-sub{top:390px;left:180px;width:840px;text-align:center;color:var(--white);font-size:17.5px;line-height:34px;font-weight:500}
.section-title{position:absolute;left:0;width:1200px;text-align:center;font-size:44px;font-weight:700;color:var(--blue);letter-spacing:.5px}
.section-title span{color:var(--muted);font-weight:500}
.rule{position:absolute;height:3px;background:var(--muted)}
.arrow{position:absolute;width:28px;height:28px;border-radius:50%;display:flex;align-items:center;justify-content:center}
.arrow.on{background:var(--blue)}
.arrow.off{background:#aaa}
.card{position:absolute;top:932px;width:312px;height:356px;background:var(--white);border:1px solid #e2e2e2;box-shadow:0 2px 8px rgba(0,0,0,.08);border-radius:4px;overflow:hidden}
.card .ph{position:absolute;left:2px;top:2px;right:2px;height:296px}
.card .label{position:absolute;bottom:22px;width:100%;text-align:center;font-size:18px;font-weight:500;color:#222}
.about-img{left:0;top:1468px;width:553px;height:548px;background:var(--blue)}
.about-panel{left:553px;top:1468px;width:647px;height:548px;background:var(--grey-bg)}
.about-text{left:640px;width:452px;font-size:14.5px;line-height:30px;color:var(--soft);text-align:justify}
.blog{position:absolute;top:2203px;width:314px;height:369px;background:var(--white);box-shadow:0 2px 10px rgba(0,0,0,.1)}
.blog .ph{height:210px}
.blog .tag{position:absolute;left:15px;top:224px;color:var(--blue);font-weight:700;font-size:15px}
.blog .ttl{position:absolute;left:15px;top:254px;font-size:17.5px;color:#222}
.blog .meta{position:absolute;left:15px;top:318px;font-size:13px;color:#777;display:flex;gap:32px}
.blog .meta span{display:flex;align-items:center;gap:6px}
.connect{left:0;top:2660px;width:1190px;height:598px;background:var(--grey-bg)}
.flabel{position:absolute;font-size:15.5px;color:#222}
.field{position:absolute;height:41px;background:var(--white);border:1px solid #c9c9c9;border-radius:6px;font-size:12.5px;color:#555;padding-left:16px;display:flex;align-items:center}
.info{left:733px;top:2710px;width:330px;height:505px;background:var(--blue);border-radius:28px;color:var(--white)}
.info h4{position:absolute;left:48px;font-size:23px;font-weight:700}
.info .row{position:absolute;left:45px;display:flex;align-items:center;gap:12px;font-size:16.5px}
.soc{width:29px;height:29px;border-radius:50%;background:var(--white)}
.foot-links{position:absolute;top:3434px;right:114px;display:flex;gap:16px;font-size:15px;color:#555}
</style>
</head>
<body>

<!-- Header -->
<div class="abs brand" style="left:110px;top:82px;font-size:26px;">DORVANSKI LAW</div>
<div class="abs" style="left:110px;top:114px;font-size:11px;font-weight:600;color:var(--blue);letter-spacing:3px;">PLLC</div>

<div class="abs topbar">
  <div class="item" style="left:62px">
    <svg width="22" height="22" viewBox="0 0 24 24"><circle cx="12" cy="12" r="12" fill="#fff"/><path d="M12 5a4.5 4.5 0 0 0-4.5 4.5c0 3.4 4.5 8.5 4.5 8.5s4.5-5.1 4.5-8.5A4.5 4.5 0 0 0 12 5zm0 6.2a1.7 1.7 0 1 1 0-3.4 1.7 1.7 0 0 1 0 3.4z" fill="#0a4f8f"/></svg>
    Suite B Marlow, Texas 77450</div>
  <div class="item" style="left:333px">
    <svg width="22" height="22" viewBox="0 0 24 24"><circle cx="12" cy="12" r="12" fill="#fff"/><path d="M8.6 6.5l1.8-.3 1.1 2.7-1.3 1a7 7 0 0 0 3.6 3.6l1-1.3 2.7 1.1-.3 1.8c-.1.5-.5.9-1.1.9A9.5 9.5 0 0 1 7.6 7.6c0-.6.4-1 1-1.1z" fill="#0a4f8f"/></svg>
    (409) 555-0172</div>
  <div class="item" style="left:546px">
    <svg width="22" height="22" viewBox="0 0 24 24"><circle cx="12" cy="12" r="12" fill="#fff"/><path d="M12 6v6l4 2" stroke="#0a4f8f" stroke-width="2" fill="none" stroke-linecap="round"/></svg>
    Mon - Fri &nbsp;8AM - 5PM</div>
</div>

<nav class="abs nav">
  <span class="active">Home</span><span>Practices</span><span>Areas</span><span>About Me</span><span>Blog</span>
</nav>
<div class="btn muted" style="left:832px;top:74px;width:256px;height:47px;">Schedule a consultation</div>

<!-- Hero -->
<div class="abs hero-photo" role="img" aria-label="Dim library with marble busts and shelves of old leather-bound books"></div>
<div class="abs" style="left:0;top:132px;width:1200px;height:680px;background:rgba(0,0,0,.35)"></div>
<h1 class="abs hero-title">PERSONAL LEGAL SOLUTIONS IN<br>LIFE'S MOST DIFFICULT MOMENTS</h1>
<p class="abs hero-sub">Helping clients navigate probate, guardianships, estate planning, and other civil disputes by providing personal attention to each client; knowing their objectives; understanding their needs; and then thinking creatively to achieve those goals.</p>
<div class="btn" style="left:381px;top:528px;width:274px;height:47px;">Schedule a consultation</div>
<div class="btn muted" style="left:673px;top:528px;width:127px;height:47px;">Read more</div>

<svg class="abs" style="left:0;top:630px" width="1200" height="190" viewBox="0 0 1200 190">
  <polygon points="0,42 288,148 600,10 935,148 1200,30 1200,190 0,190" fill="#0a4f8f"/>
  <polygon points="0,72 288,178 600,40 935,160 1200,52 1200,190 0,190" fill="#fff"/>
</svg>

<!-- Practice Areas -->
<h2 class="section-title" style="top:815px;">PRACTICE <span>AREAS</span></h2>
<div class="rule" style="left:544px;top:882px;width:114px;"></div>

<div class="arrow on" style="left:40px;top:1105px"><svg width="12" height="12" viewBox="0 0 12 12"><path d="M8 1L3 6l5 5" stroke="#fff" stroke-width="2" fill="none"/></svg></div>
<div class="arrow off" style="left:1128px;top:1105px"><svg width="12" height="12" viewBox="0 0 12 12"><path d="M4 1l5 5-5 5" stroke="#fff" stroke-width="2" fill="none"/></svg></div>

<div class="card" style="left:110px">
  <div class="ph" role="img" aria-label="Hand signing a document on a clipboard" style="background:linear-gradient(135deg,#2b2926,#8a8378 55%,#d9d4cc)"></div>
  <div class="label">Probate and Trusts</div>
</div>
<div class="card" style="left:443px">
  <div class="ph" role="img" aria-label="Couple meeting an advisor in a bright room" style="height:160px;background:linear-gradient(135deg,#bfc4c6,#e6e6e2 60%,#9aa3a8);clip-path:polygon(0 0,100% 0,100% 68%,50% 100%,0 68%)"></div>
  <div class="abs" style="left:133px;top:146px;width:46px;height:46px;border-radius:50%;background:var(--blue);border:3px solid #fff;display:flex;align-items:center;justify-content:center">
    <svg width="20" height="20" viewBox="0 0 20 20"><path d="M10 2L3 7v11h14V7z" fill="#fff"/><rect x="8" y="11" width="4" height="7" fill="#0a4f8f"/></svg>
  </div>
  <div class="abs" style="top:205px;width:100%;text-align:center;font-size:21px;font-weight:700;color:var(--blue)">Estate Planning</div>
  <div class="abs" style="top:244px;left:20px;width:272px;text-align:center;font-size:11.5px;line-height:24px;color:#777">Helping individuals and families create tailored plans that safeguard their assets, ensure their wishes are fulfilled, and provide for their loved ones after they pass away.</div>
</div>
<div class="card" style="left:778px">
  <div class="ph" role="img" aria-label="Proud father with graduate daughter in cap and gown" style="background:linear-gradient(135deg,#7e8a93,#c9cdd0 50%,#3a3a40)"></div>
  <div class="label">Adult Guardianships</div>
</div>

<div class="btn" style="left:463px;top:1320px;width:274px;height:47px;">Schedule a consultation</div>

<!-- About -->
<div class="abs about-img" role="img" aria-label="Portrait of the attorney in a navy suit and red tie on a blue background"></div>
<div class="abs about-panel"></div>
<h2 class="abs" style="left:645px;top:1515px;font-size:44px;font-weight:700;color:var(--blue)">ABOUT <span style="color:var(--muted);font-weight:500">ME</span></h2>
<div class="rule" style="left:645px;top:1580px;width:112px;"></div>
<p class="abs about-text" style="top:1618px">It is my honor to provide quality legal services at a easonable price to clients that I enjoy working with and for. I am grateful for all my clients and the trust they place in me to represent them.</p>
<p class="abs about-text" style="top:1752px">My practice focuses on Probate, Adult Guardianships, and Trust Administration and Litigation. I also represent clients in other general civil litigation matters. &nbsp;Finally, I handle estate planning for families of modest means.</p>
<div class="btn" style="left:643px;top:1890px;width:127px;height:48px;">Read more</div>

<!-- Blog -->
<h2 class="section-title" style="top:2095px;">Recent <span>Blog</span></h2>
<div class="rule" style="left:543px;top:2160px;width:114px;"></div>

<div class="arrow on" style="left:34px;top:2333px"><svg width="12" height="12" viewBox="0 0 12 12"><path d="M8 1L3 6l5 5" stroke="#fff" stroke-width="2" fill="none"/></svg></div>
<div class="arrow off" style="left:1123px;top:2333px"><svg width="12" height="12" viewBox="0 0 12 12"><path d="M4 1l5 5-5 5" stroke="#fff" stroke-width="2" fill="none"/></svg></div>

<div class="blog" style="left:112px">
  <div class="ph" role="img" aria-label="Lawyer reviewing papers with a client in a wood-paneled office" style="background:linear-gradient(135deg,#d6cfc9,#5a3a2a 55%,#2a2a33)"></div>
  <div class="tag">News</div><div class="ttl">Trusts vs. Wills</div>
  <div class="meta"><span><svg width="14" height="14" viewBox="0 0 14 14"><rect x="1" y="2" width="12" height="11" fill="none" stroke="#888"/><path d="M1 5h12" stroke="#888"/></svg>Sep 29 ,2025</span><span><svg width="22" height="14" viewBox="0 0 22 14"><rect x="1" y="1" width="20" height="10" rx="2" fill="none" stroke="#888"/><circle cx="7" cy="6" r="1" fill="#888"/><circle cx="11" cy="6" r="1" fill="#888"/><circle cx="15" cy="6" r="1" fill="#888"/></svg>4 Comments</span></div>
</div>
<div class="blog" style="left:442px">
  <div class="ph" role="img" aria-label="Business team in suits at a meeting table" style="background:linear-gradient(135deg,#3e4650,#9aa0a6 55%,#d8dadc)"></div>
  <div class="tag">News</div><div class="ttl">Why probate is needed sometimes</div>
  <div class="meta"><span><svg width="14" height="14" viewBox="0 0 14 14"><rect x="1" y="2" width="12" height="11" fill="none" stroke="#888"/><path d="M1 5h12" stroke="#888"/></svg>Sep 212025</span><span><svg width="22" height="14" viewBox="0 0 22 14"><rect x="1" y="1" width="20" height="10" rx="2" fill="none" stroke="#888"/><circle cx="7" cy="6" r="1" fill="#888"/><circle cx="11" cy="6" r="1" fill="#888"/><circle cx="15" cy="6" r="1" fill="#888"/></svg>4 Comments</span></div>
</div>
<div class="blog" style="left:772px">
  <div class="ph" role="img" aria-label="Colleagues discussing documents in a bright office" style="background:linear-gradient(135deg,#e4e6e8,#9ea6ad 50%,#4a4f55)"></div>
  <div class="tag">News</div><div class="ttl">Estate Planning Essentials</div>
  <div class="meta"><span><svg width="14" height="14" viewBox="0 0 14 14"><rect x="1" y="2" width="12" height="11" fill="none" stroke="#888"/><path d="M1 5h12" stroke="#888"/></svg>Sep 15 ,2025</span><span><svg width="22" height="14" viewBox="0 0 22 14"><rect x="1" y="1" width="20" height="10" rx="2" fill="none" stroke="#888"/><circle cx="7" cy="6" r="1" fill="#888"/><circle cx="11" cy="6" r="1" fill="#888"/><circle cx="15" cy="6" r="1" fill="#888"/></svg>4 Comments</span></div>
</div>

<!-- Connect -->
<div class="abs connect"></div>
<h2 class="abs" style="left:108px;top:2710px;font-size:43px;font-weight:700;color:var(--blue)">LET’S CONNECT <span style="color:var(--muted);font-weight:500">WITH US</span></h2>
<div class="rule" style="left:108px;top:2770px;width:118px;"></div>

<div class="flabel" style="left:108px;top:2826px">First Name *</div>
<div class="flabel" style="left:391px;top:2826px">Last Name*</div>
<div class="field" style="left:111px;top:2866px;width:258px">Ex.David</div>
<div class="field" style="left:394px;top:2866px;width:258px">Ex.David</div>
<div class="flabel" style="left:108px;top:2938px">Email *</div>
<div class="flabel" style="left:391px;top:2938px">Phone Number*</div>
<div class="field" style="left:111px;top:2977px;width:258px">Ex.David</div>
<div class="field" style="left:394px;top:2977px;width:258px">Enter Phone Number</div>
<div class="flabel" style="left:111px;top:3042px">Your Messsage *</div>
<div class="field" style="left:114px;top:3081px;width:535px">Enter Here..</div>
<div class="btn" style="left:113px;top:3158px;width:102px;height:47px;">Submit</div>

<div class="abs info">
  <h4 style="top:45px">Address</h4>
  <div class="row" style="top:90px"><svg width="26" height="26" viewBox="0 0 24 24"><circle cx="12" cy="12" r="12" fill="#fff"/><path d="M12 5a4.5 4.5 0 0 0-4.5 4.5c0 3.4 4.5 8.5 4.5 8.5s4.5-5.1 4.5-8.5A4.5 4.5 0 0 0 12 5zm0 6.2a1.7 1.7 0 1 1 0-3.4 1.7 1.7 0 0 1 0 3.4z" fill="#0a4f8f"/></svg>Lore Ipsum,USA -437916</div>
  <h4 style="top:162px">Contact</h4>
  <div class="row" style="top:209px"><svg width="26" height="26" viewBox="0 0 24 24"><circle cx="12" cy="12" r="12" fill="#fff"/><path d="M8.6 6.5l1.8-.3 1.1 2.7-1.3 1a7 7 0 0 0 3.6 3.6l1-1.3 2.7 1.1-.3 1.8c-.1.5-.5.9-1.1.9A9.5 9.5 0 0 1 7.6 7.6c0-.6.4-1 1-1.1z" fill="#0a4f8f"/></svg>(409) 555-0172</div>
  <h4 style="top:276px">Open Time</h4>
  <div class="row" style="top:315px"><svg width="26" height="26" viewBox="0 0 24 24"><circle cx="12" cy="12" r="12" fill="#fff"/><path d="M12 6v6l4 2" stroke="#0a4f8f" stroke-width="2" fill="none" stroke-linecap="round"/></svg>Mon - Fri &nbsp;8AM - 5PM</div>
  <h4 style="top:401px">Stay Connected</h4>
  <div class="row" style="top:455px;gap:5px"><span class="soc"></span><span class="soc"></span><span class="soc"></span><span class="soc"></span><span class="soc"></span></div>
</div>

<!-- Footer -->
<div class="abs brand" style="left:108px;top:3425px;font-size:30px;">DORVANSKI LAW</div>
<div class="abs" style="left:215px;top:3462px;font-size:14px;font-weight:600;color:var(--blue);letter-spacing:3px;">PLLC</div>

<div class="abs" style="left:596px;top:3348px;width:492px;height:57px;border:1px solid #bbb;border-radius:6px;background:#fff;font-size:14px;color:#666;padding-left:13px;display:flex;align-items:center">Enter Email Address</div>
<div class="abs" style="left:1025px;top:3348px;width:63px;height:57px;background:var(--blue);border-radius:0 6px 6px 0;display:flex;align-items:center;justify-content:center">
  <svg width="30" height="30" viewBox="0 0 24 24"><path d="M3 11L21 3l-8 18-2-8z" fill="none" stroke="#fff" stroke-width="2" stroke-linejoin="round"/><path d="M11 13l10-10" stroke="#fff" stroke-width="2"/></svg>
</div>
<div class="foot-links"><span>Home</span><span>|</span><span>Practices</span><span>|</span><span>Areas</span><span>|</span><span>About Me</span><span>|</span><span>Blog</span></div>
<div class="abs" style="left:112px;top:3500px;width:978px;height:2px;background:var(--blue)"></div>
<div class="abs" style="left:0;top:3516px;width:1200px;text-align:center;font-size:11px;color:#333">© 2025 Dorvanski Law, PLLC | All Rights Reserved</div>

</body>
</html>
```